Business card

I want a business card the looks like a credit card, must eye-catching !!! I attached some things that I did obviously I want it to LOOK WAY more professional than what I can do....Just some ideas.... that I was thinking

Contact Information for Business Card

Must look like a credit card, I attached some things that I did obviously I want it to LOOK WAY more professional than what I can do....Just some ideas.... that I was thinking

Requirements
Must have
• Must look like a credit card, I attached some things that I did obviously I want it to LOOK WAY more professional than what I can do....Just some ideas.... that I was thinking
Nice to have
Should not have

```html
<!DOCTYPE html>
<html lang="en">
<head>
<meta charset="utf-8">
<title>Business Card – Card Back</title>
<link rel="stylesheet" href="https://fonts.googleapis.com/css2?family=Arimo:wght@400;700&family=Great+Vibes&display=swap">
<style>
  :root {
    --card-edge: #8d8db4;
    --card-center: #8dbde0;
    --stripe-black: #000000;
    --panel-white: #ffffff;
    --ink: #111111;
    --brand-ink: #1b4f8a;
    --tag-ink: #1b1f3a;
  }
  html, body {
    margin: 0;
    padding: 0;
    width: 1200px;
    height: 749px;
    overflow: hidden;
  }
  .card-back {
    position: relative;
    width: 1200px;
    height: 749px;
    background: radial-gradient(ellipse 60% 75% at 55% 45%, var(--card-center) 0%, #93abd3 55%, var(--card-edge) 100%);
    overflow: hidden;
    font-family: "Arimo", Arial, sans-serif;
  }
  .magnetic-stripe {
    position: absolute;
    left: 0;
    top: 121px;
    width: 1200px;
    height: 127px;
    background: var(--stripe-black);
  }
  .signature-panel {
    position: absolute;
    left: 0;
    top: 263px;
    width: 1200px;
    height: 127px;
    background: var(--panel-white);
  }
  .signature-slogan {
    position: absolute;
    left: 112px;
    top: 285px;
    width: 976px;
    margin: 0;
    font-family: "Great Vibes", cursive;
    font-size: 64px;
    font-weight: 400;
    line-height: 1.2;
    color: var(--ink);
    white-space: nowrap;
    text-align: center;
  }
  .panel-label {
    position: absolute;
    top: 408px;
    margin: 0;
    font-size: 20px;
    color: var(--ink);
    letter-spacing: 0.3px;
  }
  .panel-label--left { left: 112px; }
  .panel-label--right { right: 120px; }

  .company-block {
    position: absolute;
    right: 40px;
    top: 590px;
    text-align: right;
  }
  .company-name {
    margin: 0;
    font-size: 34px;
    font-weight: 700;
    line-height: 1.15;
    color: var(--brand-ink);
    white-space: nowrap;
  }
  .company-services {
    margin: 10px 0 0;
    font-size: 15px;
    font-weight: 700;
    line-height: 1.5;
    color: var(--tag-ink);
    letter-spacing: 0.3px;
    white-space: nowrap;
  }
</style>
</head>
<body>
  <div class="card-back">
    <div class="magnetic-stripe"></div>
    <div class="signature-panel"></div>
    <p class="signature-slogan">Experience Better Credit Card Processing</p>
    <p class="panel-label panel-label--left">AUTHORIZED SIGNATURE</p>
    <p class="panel-label panel-label--right">NOT VALID UNLESS SIGNED</p>

    <div class="company-block">
      <p class="company-name">Northgate Business Solution</p>
      <p class="company-services">BUSINESS BROKER · BUSINESS FUNDING<br>CREDIT CARD PROCESSING · MERCHANT BROKER</p>
    </div>
  </div>
</body>
</html>
```